Business card design needed

We are a independent software development company specialising in financial and business custom applications and Verlane Suite automation and integration.
Colours: Blue/Purple/Yellow/White
Target Market(s)
CFO's, CIO's, Financial Managers, Business Managers
Industry/Entity Type
Financial
Contact Information for Business Card
Dennis P Holtby
MR Systems (QLD) Pty Ltd
ABN: 64 905 218 473
PO Box 817
Harwick Point Qld 4619
Mobile: 0412 739 064
Email: programmer@mr-systems.example
Web: www.mr-systems.example
Brevlo logo, Plazzo logo
Logo styles of interest
Abstract Logo
Requirements
Must have
- Flat screen computer monitor keyboard and mouse
Nice to have
- would like to see some binary digits ie. 1's and 0's incorporated in the background.

```html
<!DOCTYPE html>
<html lang="en">
<head>
<meta charset="utf-8">
<title>MR Systems – Business Card</title>
<link rel="stylesheet" href="https://fonts.googleapis.com/css2?family=Poppins:wght@400;600&family=Open+Sans:wght@400;700&display=swap">
<style>
  :root {
    --page-bg: #e6e6e8;
    --card-white: #ffffff;
    --brand-purple: #4f2d84;
    --photo-deep: #1d1436;
    --photo-violet: #7a3fb0;
    --photo-lilac: #b58fd6;
    --ink: #1f1f24;
    --ink-soft: #3a3a40;
    --icon-ink: #4a4a52;
  }
  * { margin: 0; padding: 0; box-sizing: border-box; }
  html, body {
    width: 1200px;
    height: 823px;
    overflow: hidden;
    background: var(--page-bg);
  }
  .canvas {
    position: relative;
    width: 1200px;
    height: 823px;
  }
  .card {
    position: absolute;
    left: 65px;
    top: 112px;
    width: 1069px;
    height: 598px;
    background: var(--card-white);
    overflow: hidden;
    box-shadow: 0 2px 10px rgba(0,0,0,0.18);
  }
  .card-shapes {
    position: absolute;
    inset: 0;
  }
  .social {
    position: absolute;
    top: 92px;
    left: 178px;
    display: flex;
    gap: 26px;
    font-family: "Poppins", sans-serif;
    font-weight: 600;
    font-size: 22px;
    color: var(--card-white);
  }
  .social-item {
    display: flex;
    align-items: center;
    gap: 8px;
  }
  .social-mark {
    width: 16px;
    height: 16px;
    background: var(--card-white);
  }
  .identity {
    position: absolute;
    left: 466px;
    top: 128px;
    transform: rotate(-9deg);
    transform-origin: left bottom;
    color: var(--card-white);
    font-family: "Poppins", sans-serif;
  }
  .identity-name {
    font-weight: 600;
    font-size: 50px;
    line-height: 1;
    letter-spacing: 0.5px;
  }
  .identity-company {
    margin-top: 26px;
    margin-left: 14px;
    font-weight: 400;
    font-size: 27px;
    line-height: 1;
  }
  .contact {
    position: absolute;
    left: 462px;
    top: 318px;
    transform: rotate(-9deg);
    transform-origin: left top;
    font-family: "Open Sans", sans-serif;
  }
  .contact-line {
    display: flex;
    align-items: center;
    gap: 16px;
    height: 48px;
    font-weight: 700;
    font-size: 26px;
    color: var(--ink);
  }
  .contact-icon {
    width: 28px;
    height: 30px;
    flex: none;
  }
  .contact-address {
    margin-top: 22px;
    margin-left: 80px;
    font-weight: 400;
    font-size: 26px;
    line-height: 1.35;
    color: var(--ink-soft);
  }
</style>
</head>
<body>
<main class="canvas">
  <article class="card">
    <svg class="card-shapes" width="1069" height="598" viewBox="0 0 1069 598" xmlns="http://www.w3.org/2000/svg">
      <defs>
        <linearGradient id="photoTone" x1="0" y1="0" x2="0.6" y2="1">
          <stop offset="0" stop-color="var(--photo-violet)"/>
          <stop offset="0.45" stop-color="var(--photo-lilac)"/>
          <stop offset="1" stop-color="var(--photo-deep)"/>
        </linearGradient>
      </defs>
      <polygon points="0,0 367,0 472,598 0,598" fill="url(#photoTone)" role="img" aria-label="Illustration of a flat screen monitor, keyboard and mouse over purple abstract light with binary digits"/>
      <polygon class="name-band" points="367,0 1069,0 1069,185 421,310" fill="var(--brand-purple)"/>
    </svg>

    <div class="social">
      <span class="social-item"><span class="social-mark"></span>Plazzo</span>
      <span class="social-item"><span class="social-mark"></span>Brevlo</span>
    </div>

    <header class="identity">
      <h1 class="identity-name">Dennis P Holtby</h1>
      <p class="identity-company">MR Systems (QLD) Pty Ltd</p>
    </header>

    <section class="contact">
      <p class="contact-line">
        <svg class="contact-icon" viewBox="0 0 28 30" aria-hidden="true">
          <rect x="7" y="2" width="14" height="26" rx="2.5" fill="none" stroke="var(--icon-ink)" stroke-width="2"/>
          <line x1="7" y1="22" x2="21" y2="22" stroke="var(--icon-ink)" stroke-width="1.5"/>
          <circle cx="14" cy="25" r="1.2" fill="var(--icon-ink)"/>
        </svg>
        0412 739 064
      </p>
      <p class="contact-line">
        <svg class="contact-icon" viewBox="0 0 28 30" aria-hidden="true">
          <rect x="2" y="8" width="24" height="16" fill="none" stroke="var(--icon-ink)" stroke-width="1.8"/>
          <polyline points="2,8 14,18 26,8" fill="none" stroke="var(--icon-ink)" stroke-width="1.8"/>
        </svg>
        programmer@mr-systems.example
      </p>
      <p class="contact-line">
        <svg class="contact-icon" viewBox="0 0 28 30" aria-hidden="true">
          <circle cx="14" cy="15" r="11" fill="none" stroke="var(--icon-ink)" stroke-width="1.6"/>
          <ellipse cx="14" cy="15" rx="5" ry="11" fill="none" stroke="var(--icon-ink)" stroke-width="1.4"/>
          <line x1="3" y1="15" x2="25" y2="15" stroke="var(--icon-ink)" stroke-width="1.4"/>
          <line x1="5" y1="9" x2="23" y2="9" stroke="var(--icon-ink)" stroke-width="1.2"/>
          <line x1="5" y1="21" x2="23" y2="21" stroke="var(--icon-ink)" stroke-width="1.2"/>
        </svg>
        www.mr-systems.example
      </p>
      <address class="contact-address" style="font-style:normal">
        PO Box 817<br>
        Harwick Point Qld 4619
      </address>
    </section>
  </article>
</main>
</body>
</html>
```